Brightkoru NZ Brand, Revenue, Promotions & Events

I need an innovative business card that pops my brand. I like the colours against darker gradients and i'm not afraid to be bold.

I run my own Business, Brand, Event & Promotion company. I specialise in breathing life into businesses and adding atmosphere to promotions and events. I am concept based lady that likes to test the boundaries and create stand out campaigns that connect with the consumer.

I have 12 years business experience in a realm of interesting fields form 11 years in coordinating international music festivals & promotions, 6 years in radio with 8 radio awards including a NZ radio award for best sales team in NZ and was the national brand and sales manager for New Zealands 1st indoor entertainment mall. With 10 years of experience in advertising sales, I have an eye for creating revenue streams for businesses and thrive on implementing campaigns that compliment those streams.

I love sayings like "Do what you love, love what you do" and believe that you can achieve anything you want.

I have been fortunate in my career that my connections have carried me without needing to promote my business however it is important that I start to do so.

Target Market(s)

Decision makers 25 to 54

Contact Information for Business Card

Petra Holsworth
Director
p. 022 739 5081
e. petra@brightkoru.example
www.brightkoru.example

FB, IG and Linkedin logo

Font styles to use
Sans Serif

Colors

Designer to choose colors to be used in the design.

Requirements
Must have
• Petra Holsworth
• Director
• p. 022 739 5081
• e. petra@brightkoru.example
• www.brightkoru.example
• FB, IG and Linkedin logo
Nice to have
• I am looking for a business card with character, that leaves my presence with my customer and makes them remember my brand & optimistic personality when i walk out the door.

```html
<!DOCTYPE html>
<html lang="en">
<head>
<meta charset="utf-8">
<title>Brightkoru NZ – Business Card</title>
<link rel="stylesheet" href="https://fonts.googleapis.com/css2?family=Montserrat:wght@400;500;700&display=swap">
<style>
  :root {
    --stage: #2b2b2d;
    --card-top: #1c1c1e;
    --card-bottom: #0c0c0d;
    --accent: #29a9e1;
    --text-grey: #9a9a9c;
    --text-light: #b8b8ba;
    --rule: #4a4a4c;
    --ghost: #050505;
  }
  * { margin: 0; padding: 0; box-sizing: border-box; }
  html, body { width: 1200px; height: 900px; overflow: hidden; }
  body {
    background: var(--stage);
    font-family: "Montserrat", Arial, sans-serif;
    display: flex;
    flex-direction: column;
    align-items: center;
    justify-content: center;
    gap: 40px;
  }
  .card {
    position: relative;
    width: 580px;
    height: 330px;
    background: linear-gradient(160deg, var(--card-top), var(--card-bottom));
    overflow: hidden;
    text-align: center;
    color: var(--text-light);
  }
  .card::after {
    content: "";
    position: absolute;
    left: 0; right: 0; bottom: 0;
    height: 9px;
    background: var(--accent);
  }

  /* front */
  .brand-lockup {
    position: absolute;
    top: 92px; left: 0; right: 0;
  }
  .brand-name {
    display: inline-flex;
    align-items: center;
    gap: 12px;
    font-size: 40px;
    font-weight: 500;
    letter-spacing: 3px;
    color: var(--accent);
    text-transform: uppercase;
  }
  .brand-dot {
    width: 18px; height: 18px;
    border-radius: 50%;
    background: var(--accent);
  }
  .brand-services {
    margin-top: 4px;
    font-size: 13px;
    letter-spacing: 1.5px;
    color: var(--text-grey);
    text-transform: uppercase;
  }
  .slogan {
    position: absolute;
    bottom: 58px; left: 0; right: 0;
    font-size: 16px;
    font-weight: 700;
    letter-spacing: 0.5px;
    color: var(--text-grey);
  }

  /* back */
  .ghost-name {
    position: absolute;
    top: 118px; left: 0; right: 0;
    font-size: 54px;
    font-weight: 500;
    letter-spacing: 4px;
    color: var(--ghost);
    text-transform: uppercase;
  }
  .contact {
    position: absolute;
    top: 52px; left: 0; right: 0;
  }
  .person-name {
    font-size: 19px;
    font-weight: 700;
    color: var(--accent);
    letter-spacing: 0.5px;
  }
  .person-role {
    font-size: 14px;
    color: var(--text-grey);
    margin-top: 2px;
  }
  .divider-row {
    display: flex;
    align-items: center;
    justify-content: center;
    gap: 10px;
    margin: 8px auto;
    width: 260px;
  }
  .divider-row::before, .divider-row::after {
    content: "";
    flex: 1;
    height: 1px;
    background: var(--rule);
  }
  .icon-square {
    width: 24px; height: 24px;
    border-radius: 3px;
    background: var(--accent);
    display: flex; align-items: center; justify-content: center;
  }
  .icon-circle {
    width: 24px; height: 24px;
    border-radius: 50%;
    border: 1.5px solid var(--accent);
  }
  .contact-lines {
    font-size: 15px;
    line-height: 1.35;
    color: var(--text-light);
  }
  .contact-lines .web-highlight { color: var(--accent); }
</style>
</head>
<body>

<section class="card card-front">
  <div class="brand-lockup">
    <div class="brand-name"><span class="brand-dot"></span>Brightkoru NZ</div>
    <div class="brand-services">Brand | Revenue | Events &amp; Promotions</div>
  </div>
  <p class="slogan">DO WHAT YOU LOVE, LOVE WHAT YOU DO</p>
</section>

<section class="card card-back">
  <div class="ghost-name" aria-hidden="true">Brightkoru NZ</div>
  <div class="contact">
    <h1 class="person-name">PETRA HOLSWORTH</h1>
    <p class="person-role">Director</p>
    <div class="divider-row">
      <span class="icon-square" aria-label="phone">
        <svg width="14" height="14" viewBox="0 0 24 24"><path fill="#111" d="M6.6 10.8a15 15 0 0 0 6.6 6.6l2.2-2.2c.3-.3.7-.4 1-.2 1.1.4 2.3.6 3.6.6.6 0 1 .4 1 1V20c0 .6-.4 1-1 1A17 17 0 0 1 3 4c0-.6.4-1 1-1h3.5c.6 0 1 .4 1 1 0 1.3.2 2.5.6 3.6.1.3 0 .7-.2 1z"/></svg>
      </span>
      <span class="icon-square" aria-label="email">
        <svg width="14" height="14" viewBox="0 0 24 24"><rect x="2" y="5" width="20" height="14" fill="none" stroke="#111" stroke-width="2.2"/><path d="M2 6l10 7 10-7" fill="none" stroke="#111" stroke-width="2.2"/></svg>
      </span>
      <span class="icon-square" aria-label="website">
        <svg width="14" height="14" viewBox="0 0 24 24"><circle cx="12" cy="12" r="9" fill="none" stroke="#111" stroke-width="2.2"/><path d="M3 12h18M12 3c3 3 3 15 0 18M12 3c-3 3-3 15 0 18" fill="none" stroke="#111" stroke-width="1.8"/></svg>
      </span>
    </div>
    <div class="contact-lines">
      <p>022 739 5081</p>
      <p>petra@brightkoru.example</p>
      <p>www.<span class="web-highlight">brightkoru</span>.example</p>
    </div>
    <div class="divider-row">
      <span class="icon-circle" aria-label="social profile"></span>
      <span class="icon-circle" aria-label="social profile"></span>
      <span class="icon-circle" aria-label="social profile"></span>
    </div>
  </div>
</section>

</body>
</html>
```